依頼詳細
■デザインのイメージ
・通りがかりでもパッと目を引くようなデザインでお願いします。
・ノマドカフェとバナナジュースのお店であることがパッと見てわかるようなデザインでお願いいたします。
・店内で使用しているメニュー表やのぼりの旗などのデザインと統一性を持たせつつも、タペストリーはシンプルに仕上げられたらと思っております。
・メインカラーが黄色で、サブカラーは #5ABEC2くらいの水色でお願いします。
・参考になりそうなタペストリー(ワイン食堂のお店とバナナジュースのお店)も添付させていただいております。

■ターゲット層
フリーランス、大学生(テイクアウトで高校生も想定)、その他
記載項目
・デザインに使用するロゴは縦と横(白縁ありとなし)がございますので、添付しております。
・参考にしていただきたい、当店のメニュー表やのぼりの旗のデザインも添付しております。
・またInstagram( https://www.fotolane.net/kumo.mikan/ )でお店の雰囲気も参考にしていただけますと幸いです。
・Instagramの画像は自由にご使用くださいませ。実際にご依頼となりましたら、元データをお送りさせていただくことが可能です。
希望イメージ
シンプル 複雑
単色 カラフル
暗い 明るい
日常 高級
遊び心 厳粛
未来的 伝統的
女性的 男性的
希望する色
黄・オレンジ系、水色系
納品ファイル
• 高解像度JPG (.jpg)
• イラストレーター形式 (.ai)
• PNG形式 (.png)
補足説明
■ 選んだ理由

外観に飾るタペストリーということで、パッと目を引くデザインがいいなと思っていたのですが、キャラクターを大きくデザインするという当方では思いつかないデザインがとても魅力的でした!

■ 提案者全員のお礼・コメント

この度は、たくさんの素敵なデザインをご提案いただきまして、誠にありがとうございました!

```html
<!DOCTYPE html>
<html lang="ja">
<head>
<meta charset="UTF-8">
<title>くもみかん Tapestry</title>
<link href="https://fonts.googleapis.com/css2?family=M+PLUS+Rounded+1c:wght@800&display=swap" rel="stylesheet">
<style>
  :root {
    --page: #ffffff;
    --banana: #f7dd5a;
    --stripe-blue: #8fcfe0;
    --stripe-yellow: #f7dd5a;
    --ink: #1a1a1a;
    --badge: #ffffff;
    --char-brown: #a8733e;
    --char-light: #e9c48e;
  }
  * { margin: 0; padding: 0; box-sizing: border-box; }
  html, body {
    width: 846px;
    height: 1200px;
    overflow: hidden;
    background: var(--page);
  }
  .canvas {
    position: relative;
    width: 846px;
    height: 1200px;
  }
  .tapestry {
    position: absolute;
    left: 113px;
    top: 85px;
    width: 615px;
    height: 1015px;
    background: var(--banana);
    overflow: hidden;
  }
  .stripe-band {
    position: absolute;
    left: 0;
    width: 100%;
    background: repeating-linear-gradient(
      90deg,
      var(--stripe-blue) 0 26px,
      var(--stripe-yellow) 26px 52px
    );
  }
  .stripe-band.top { top: 0; height: 122px; }
  .stripe-band.bottom { bottom: 0; height: 98px; }
  .logo-badge {
    position: absolute;
    left: 124px;
    top: 90px;
    width: 366px;
    height: 366px;
    border-radius: 50%;
    background: var(--badge);
  }
  .character {
    position: absolute;
    left: 123px;
    top: 50px;
    width: 120px;
    height: 150px;
    border-radius: 50% 50% 40% 40%;
    background: radial-gradient(circle at 50% 40%, var(--char-light), var(--char-brown));
  }
  .brand-name {
    position: absolute;
    left: 0;
    top: 222px;
    width: 100%;
    text-align: center;
    font-family: "M PLUS Rounded 1c", sans-serif;
    font-weight: 800;
    color: var(--ink);
    font-size: 46px;
    line-height: 1;
  }
  .brand-sub {
    position: absolute;
    left: 0;
    top: 280px;
    width: 100%;
    text-align: center;
    font-family: "M PLUS Rounded 1c", sans-serif;
    font-weight: 800;
    color: var(--ink);
    font-size: 17px;
  }
  .tagline {
    position: absolute;
    left: 0;
    top: 600px;
    width: 100%;
    text-align: center;
    font-family: "M PLUS Rounded 1c", sans-serif;
    font-weight: 800;
    color: var(--ink);
    font-size: 44px;
    line-height: 1.12;
  }
</style>
</head>
<body>
  <div class="canvas">
    <div class="tapestry">
      <div class="stripe-band top"></div>

      <div class="logo-badge">
        <div class="character" role="img" aria-label="Cartoon mascot holding a bunch of bananas"></div>
        <div class="brand-name">くもみかん</div>
        <div class="brand-sub">Kumo Mikan</div>
      </div>

      <p class="tagline">Nomad Cafe<br>&amp;<br>Banana Juice</p>

      <div class="stripe-band bottom"></div>
    </div>
  </div>
</body>
</html>
```